Culture Blueprint

I would like to edit the design of this culture blueprint graphic to align with my brand colors and services graphic. Please
The ROAM stands for Leadership, Engagement, Activate Culture and Distinguish.
Work to be done:
1. Please make Purpose in red brand "roam" color
2. Please make Philosophy in grey brand "engage" color
3. Please make Priorities in and Processes (internal and external) in orange brand "active" color
4. Please make projections in teal "distinguish" color

Creativity welcomed!

```html
<!DOCTYPE html>
<html lang="en">
<head>
<meta charset="utf-8">
<title>Alignment of the Five Ps</title>
<link rel="stylesheet" href="https://fonts.googleapis.com/css2?family=Abril+Fatface&family=Arimo:wght@700&display=swap">
<style>
  :root {
    --roam-red: #d42a3a;
    --engage-grey: #5b5d60;
    --active-orange: #ee6046;
    --distinguish-teal: #0f8f9a;
    --ink: #1d1b1b;
    --arrow-grey: #d6d6d6;
    --paper: #ffffff;
  }
  html, body {
    margin: 0;
    padding: 0;
    width: 1200px;
    height: 1168px;
    overflow: hidden;
    background: var(--paper);
  }
  .blueprint { display: block; width: 1200px; height: 1168px; }
  .title {
    font-family: "Arimo", Arial, sans-serif;
    font-weight: 700;
    font-size: 46px;
    fill: var(--ink);
  }
  .ring-line { fill: none; stroke: var(--ink); stroke-width: 1.6; }
  .divider { stroke: var(--ink); stroke-width: 1.6; }
  .flow-arrow {
    stroke: var(--arrow-grey);
    stroke-width: 12;
    fill: none;
    opacity: 0.85;
  }
  .arrow-head { fill: var(--arrow-grey); }
  .label { font-family: "Abril Fatface", "Times New Roman", serif; }
  .purpose { fill: var(--roam-red); font-size: 33px; }
  .philosophy { fill: var(--engage-grey); font-size: 34px; }
  .priorities { fill: var(--active-orange); font-size: 32px; }
  .practice { fill: var(--active-orange); font-size: 21px; }
  .practice-pair { fill: var(--active-orange); font-size: 19px; }
  .projection { fill: var(--distinguish-teal); font-size: 20px; }
  .legend-text {
    font-family: "Arimo", Arial, sans-serif;
    font-weight: 700;
    font-size: 25px;
    fill: var(--ink);
  }
  .legend-line { stroke: var(--ink); stroke-width: 2.4; fill: none; }
  .legend-head { fill: var(--ink); }
</style>
</head>
<body>
<svg class="blueprint" viewBox="0 0 1200 1168" xmlns="http://www.w3.org/2000/svg">
  <defs>
    <marker id="flow-head" viewBox="0 0 10 10" refX="5" refY="5" markerWidth="2.6" markerHeight="2.6" orient="auto-start-reverse">
      <path class="arrow-head" d="M0,0 L10,5 L0,10 z"/>
    </marker>
    <marker id="legend-head" viewBox="0 0 10 10" refX="9" refY="5" markerWidth="8" markerHeight="8" orient="auto">
      <path class="legend-head" d="M0,1 L10,5 L0,9 z"/>
    </marker>

    <!-- clockwise arcs over the top -->
    <path id="top-406" d="M126.2,573.5 A406,406 0 0 1 925.8,573.5"/>
    <path id="top-330" d="M201,586.7 A330,330 0 0 1 851,586.7"/>
    <path id="top-255" d="M274.9,599.7 A255,255 0 0 1 777.1,599.7"/>
    <path id="top-267" d="M263.1,597.6 A267,267 0 0 1 788.9,597.6"/>
    <path id="top-245" d="M284.7,601.5 A245,245 0 0 1 767.3,601.5"/>
    <path id="top-176" d="M352.7,613.4 A176,176 0 0 1 699.3,613.4"/>
    <path id="top-100" d="M427.5,626.6 A100,100 0 0 1 624.5,626.6"/>
    <!-- counter-clockwise arcs under the bottom -->
    <path id="bottom-422" d="M110.4,717.3 A422,422 0 0 0 941.6,717.3"/>
    <path id="bottom-346" d="M185.3,704.1 A346,346 0 0 0 866.7,704.1"/>
    <path id="bottom-259" d="M270.9,689 A259,259 0 0 0 781.1,689"/>
    <path id="bottom-281" d="M249.3,692.8 A281,281 0 0 0 802.7,692.8"/>
  </defs>

  <text class="title" x="600" y="103" text-anchor="middle">Alignment of the Five Ps</text>

  <!-- rings -->
  <g class="rings">
    <circle class="ring-line" cx="526" cy="644" r="74"/>
    <circle class="ring-line" cx="526" cy="644" r="150"/>
    <circle class="ring-line" cx="526" cy="644" r="225"/>
    <circle class="ring-line" cx="526" cy="644" r="301"/>
    <circle class="ring-line" cx="526" cy="644" r="376"/>
    <circle class="ring-line" cx="526" cy="644" r="452"/>
  </g>

  <!-- segment dividers -->
  <g class="dividers">
    <g class="internal-dividers">
      <line class="divider" x1="751" y1="644" x2="827" y2="644" transform="rotate(0 526 644)"/>
      <line class="divider" x1="751" y1="644" x2="827" y2="644" transform="rotate(-60 526 644)"/>
      <line class="divider" x1="751" y1="644" x2="827" y2="644" transform="rotate(-120 526 644)"/>
      <line class="divider" x1="751" y1="644" x2="827" y2="644" transform="rotate(-180 526 644)"/>
      <line class="divider" x1="751" y1="644" x2="827" y2="644" transform="rotate(-240 526 644)"/>
      <line class="divider" x1="751" y1="644" x2="827" y2="644" transform="rotate(-300 526 644)"/>
    </g>
    <g class="external-dividers">
      <line class="divider" x1="827" y1="644" x2="902" y2="644" transform="rotate(-54 526 644)"/>
      <line class="divider" x1="827" y1="644" x2="902" y2="644" transform="rotate(-126 526 644)"/>
      <line class="divider" x1="827" y1="644" x2="902" y2="644" transform="rotate(-198 526 644)"/>
      <line class="divider" x1="827" y1="644" x2="902" y2="644" transform="rotate(-270 526 644)"/>
      <line class="divider" x1="827" y1="644" x2="902" y2="644" transform="rotate(-342 526 644)"/>
    </g>
    <g class="projection-dividers">
      <line class="divider" x1="902" y1="644" x2="978" y2="644" transform="rotate(-22.5 526 644)"/>
      <line class="divider" x1="902" y1="644" x2="978" y2="644" transform="rotate(-67.5 526 644)"/>
      <line class="divider" x1="902" y1="644" x2="978" y2="644" transform="rotate(-112.5 526 644)"/>
      <line class="divider" x1="902" y1="644" x2="978" y2="644" transform="rotate(-157.5 526 644)"/>
      <line class="divider" x1="902" y1="644" x2="978" y2="644" transform="rotate(-202.5 526 644)"/>
      <line class="divider" x1="902" y1="644" x2="978" y2="644" transform="rotate(-247.5 526 644)"/>
      <line class="divider" x1="902" y1="644" x2="978" y2="644" transform="rotate(-292.5 526 644)"/>
      <line class="divider" x1="902" y1="644" x2="978" y2="644" transform="rotate(-337.5 526 644)"/>
    </g>
  </g>

  <!-- alignment arrows -->
  <g class="flow-arrows" transform="translate(526 644) scale(0.8) translate(-658 -805)">
    <line class="flow-arrow" x1="690" y1="715" x2="735" y2="350" marker-start="url(#flow-head)" marker-end="url(#flow-head)"/>
    <line class="flow-arrow" x1="662" y1="715" x2="660" y2="440" marker-start="url(#flow-head)" marker-end="url(#flow-head)"/>
    <line class="flow-arrow" x1="640" y1="715" x2="630" y2="505" marker-start="url(#flow-head)" marker-end="url(#flow-head)"/>
    <line class="flow-arrow" x1="740" y1="745" x2="965" y2="470" marker-start="url(#flow-head)" marker-end="url(#flow-head)"/>
    <line class="flow-arrow" x1="755" y1="765" x2="975" y2="660" marker-start="url(#flow-head)" marker-end="url(#flow-head)"/>
    <line class="flow-arrow" x1="745" y1="750" x2="880" y2="665" marker-start="url(#flow-head)" marker-end="url(#flow-head)"/>
    <line class="flow-arrow" x1="760" y1="822" x2="1120" y2="825" marker-start="url(#flow-head)" marker-end="url(#flow-head)"/>
    <line class="flow-arrow" x1="760" y1="855" x2="905" y2="920" marker-start="url(#flow-head)" marker-end="url(#flow-head)"/>
    <line class="flow-arrow" x1="715" y1="890" x2="870" y2="1110" marker-start="url(#flow-head)" marker-end="url(#flow-head)"/>
    <line class="flow-arrow" x1="740" y1="875" x2="975" y2="1140" marker-start="url(#flow-head)" marker-end="url(#flow-head)"/>
    <line class="flow-arrow" x1="662" y1="910" x2="690" y2="1068" marker-start="url(#flow-head)" marker-end="url(#flow-head)"/>
    <line class="flow-arrow" x1="652" y1="910" x2="658" y2="1268" marker-start="url(#flow-head)" marker-end="url(#flow-head)"/>
    <line class="flow-arrow" x1="585" y1="870" x2="335" y2="1130" marker-start="url(#flow-head)" marker-end="url(#flow-head)"/>
    <line class="flow-arrow" x1="575" y1="880" x2="435" y2="1065" marker-start="url(#flow-head)" marker-end="url(#flow-head)"/>
    <line class="flow-arrow" x1="565" y1="850" x2="425" y2="945" marker-start="url(#flow-head)" marker-end="url(#flow-head)"/>
    <line class="flow-arrow" x1="560" y1="800" x2="200" y2="800" marker-start="url(#flow-head)" marker-end="url(#flow-head)"/>
    <line class="flow-arrow" x1="560" y1="780" x2="300" y2="720" marker-start="url(#flow-head)" marker-end="url(#flow-head)"/>
    <line class="flow-arrow" x1="560" y1="760" x2="420" y2="682" marker-start="url(#flow-head)" marker-end="url(#flow-head)"/>
    <line class="flow-arrow" x1="580" y1="740" x2="315" y2="505" marker-start="url(#flow-head)" marker-end="url(#flow-head)"/>
  </g>

  <!-- core -->
  <text class="label purpose" x="526" y="656" text-anchor="middle">Purpose</text>
  <text class="label philosophy"><textPath href="#top-100" startOffset="50%" text-anchor="middle">Philosophy</textPath></text>
  <text class="label priorities"><textPath href="#top-176" startOffset="50%" text-anchor="middle">Priorities</textPath></text>

  <!-- internal practices -->
  <g class="internal-practices">
    <text class="label practice-pair"><textPath href="#top-267" startOffset="50%" text-anchor="middle">Structure, Work</textPath></text>
    <text class="label practice-pair"><textPath href="#top-245" startOffset="50%" text-anchor="middle">Design &amp; Systems</textPath></text>
    <g transform="rotate(60 526 644)">
      <text class="label practice-pair"><textPath href="#top-267" startOffset="50%" text-anchor="middle">Recruitment</textPath></text>
      <text class="label practice-pair"><textPath href="#top-245" startOffset="50%" text-anchor="middle">&amp; Selection</textPath></text>
    </g>
    <g transform="rotate(-60 526 644)">
      <text class="label practice"><textPath href="#top-255" startOffset="50%" text-anchor="middle">Technology</textPath></text>
    </g>
    <g transform="rotate(60 526 644)">
      <text class="label practice-pair"><textPath href="#bottom-259" startOffset="50%" text-anchor="middle">Internal</textPath></text>
      <text class="label practice-pair"><textPath href="#bottom-281" startOffset="50%" text-anchor="middle">Communications</textPath></text>
    </g>
    <text class="label practice-pair"><textPath href="#bottom-259" startOffset="50%" text-anchor="middle">Performance</textPath></text>
    <text class="label practice-pair"><textPath href="#bottom-281" startOffset="50%" text-anchor="middle">Management</textPath></text>
    <g transform="rotate(-60 526 644)">
      <text class="label practice-pair"><textPath href="#bottom-259" startOffset="50%" text-anchor="middle">Training &amp;</textPath></text>
      <text class="label practice-pair"><textPath href="#bottom-281" startOffset="50%" text-anchor="middle">Development</textPath></text>
    </g>
  </g>

  <!-- external practices -->
  <g class="external-practices">
    <text class="label practice"><textPath href="#top-330" startOffset="50%" text-anchor="middle">Customers</textPath></text>
    <g transform="rotate(-72 526 644)">
      <text class="label practice"><textPath href="#top-330" startOffset="50%" text-anchor="middle">Suppliers/Vendors &amp; Partners</textPath></text>
    </g>
    <g transform="rotate(72 526 644)">
      <text class="label practice"><textPath href="#top-330" startOffset="50%" text-anchor="middle">Markets</textPath></text>
    </g>
    <g transform="rotate(36 526 644)">
      <text class="label practice"><textPath href="#bottom-346" startOffset="50%" text-anchor="middle">Services</textPath></text>
    </g>
    <g transform="rotate(-36 526 644)">
      <text class="label practice"><textPath href="#bottom-346" startOffset="50%" text-anchor="middle">Products</textPath></text>
    </g>
  </g>

  <!-- projections -->
  <g class="projections">
    <text class="label projection"><textPath href="#top-406" startOffset="50%" text-anchor="middle">Name</textPath></text>
    <g transform="rotate(45 526 644)">
      <text class="label projection"><textPath href="#top-406" startOffset="50%" text-anchor="middle">Logo/Symbols</textPath></text>
    </g>
    <g transform="rotate(90 526 644)">
      <text class="label projection"><textPath href="#top-406" startOffset="50%" text-anchor="middle">Headquarters</textPath></text>
    </g>
    <g transform="rotate(-45 526 644)">
      <text class="label projection"><textPath href="#top-406" startOffset="50%" text-anchor="middle">Community Activities</textPath></text>
    </g>
    <g transform="rotate(-90 526 644)">
      <text class="label projection"><textPath href="#top-406" startOffset="50%" text-anchor="middle">Marketing/PR/Advertising</textPath></text>
    </g>
    <g transform="rotate(45 526 644)">
      <text class="label projection"><textPath href="#bottom-422" startOffset="50%" text-anchor="middle">Dress Uniforms</textPath></text>
    </g>
    <text class="label projection"><textPath href="#bottom-422" startOffset="50%" text-anchor="middle">Offices/Stores</textPath></text>
    <g transform="rotate(-45 526 644)">
      <text class="label projection"><textPath href="#bottom-422" startOffset="50%" text-anchor="middle">Leader Image</textPath></text>
    </g>
  </g>

  <!-- legend -->
  <g class="legend">
    <text class="legend-text" x="1124" y="316" text-anchor="end">Projections</text>
    <line class="legend-line" x1="1124" y1="330" x2="842" y2="330" marker-end="url(#legend-head)"/>

    <text class="legend-text" x="1124" y="407" text-anchor="end">External</text>
    <text class="legend-text" x="1124" y="439" text-anchor="end">Practices</text>
    <line class="legend-line" x1="1124" y1="448" x2="842" y2="448" marker-end="url(#legend-head)"/>

    <text class="legend-text" x="1124" y="581" text-anchor="end">Internal</text>
    <text class="legend-text" x="1124" y="612" text-anchor="end">Practices</text>
    <line class="legend-line" x1="1124" y1="621" x2="958" y2="621"/>
    <line class="legend-line" x1="915" y1="621" x2="810" y2="621" marker-end="url(#legend-head)"/>

    <text class="legend-text" x="1124" y="710" text-anchor="end">Internal</text>
    <text class="legend-text" x="1124" y="741" text-anchor="end">Practices</text>
    <polyline class="legend-line" points="1120,758 996,758 758,677" marker-end="url(#legend-head)"/>
  </g>
</svg>
</body>
</html>
```